Product Labels - Background and Layout Refresh - Made in Australia

We require 2 labels designs to be updated. One for our premium Vantora brand and a second one for our standard quality Stelko brand.
We also require a new cover for our 2018 product catalog. Attached is the current design. We need an industrial type image in the background. Text to remain the same, fonts and textures can be changed.
Vantora: MI-001-1251-P+.ai
The old Brimvale product has been replaced with the new Vantora brand. Remove the brimvale logo and use the attached Vantora logo. Change background, fonts and layout. Use the made in Australia Logo or the words Made In Australia.
Stelko: MI-001-1251.ai
The logo remains the same, the background and the fonts are to be changed and updated.
Use made in Australia Logo or the words Made In Australia.
The text and diagram content must all remain on the labels.
The design theme needs to stay very industrial and rough.
Made in Australia is a big selling point for our products, ensure that message is conveyed on the labels.
Note: The size of the disc is 125mm the size of the label is now 85mm
The layer "Background" is to show how the final product will look. Refer to .jpg for details.
Target Market(s)
Industrial user of tools
Industry/Entity Type
Industrial
Colors
Designer to choose colors to be used in the design.
Requirements
Must have
- Industrial Feel & Emphasis on Made in Australia, by text, logo or other Images
Nice to have
- Trueforge Seal Logo
Should not have
- Not playful, not fun.

```html
<!DOCTYPE html>
<html lang="en">
<head>
<meta charset="utf-8">
<title>Catalogue Fabrication Products 2018</title>
<link rel="stylesheet" href="https://fonts.googleapis.com/css2?family=Montserrat:wght@300;600;800&display=swap">
<style>
  :root {
    --ink-white: #ffffff;
    --brand-copper: #c98a2e;
    --band-dark: rgba(40, 22, 10, 0.55);
    --band-mid: rgba(70, 40, 18, 0.62);
    --rust-deep: #1e120a;
    --rust-mid: #5a3418;
    --rust-warm: #8a5a2c;
    --rust-light: #b08048;
  }
  html, body {
    margin: 0;
    padding: 0;
    width: 927px;
    height: 1200px;
    overflow: hidden;
    background: var(--rust-deep);
  }
  .cover {
    position: relative;
    width: 927px;
    height: 1200px;
    overflow: hidden;
    font-family: "Montserrat", sans-serif;
  }
  .cover-artwork {
    position: absolute;
    inset: 0;
    background:
      radial-gradient(ellipse 55% 45% at 18% 30%, var(--rust-light) 0%, transparent 70%),
      radial-gradient(ellipse 40% 55% at 5% 62%, #c9b89a 0%, transparent 65%),
      radial-gradient(ellipse 45% 40% at 80% 65%, var(--rust-warm) 0%, transparent 70%),
      radial-gradient(ellipse 50% 35% at 70% 15%, var(--rust-mid) 0%, transparent 75%),
      linear-gradient(160deg, var(--rust-mid) 0%, var(--rust-deep) 55%, #3a2212 100%);
  }
  .masthead {
    position: absolute;
    top: 0;
    left: 0;
    width: 927px;
    height: 128px;
    background: var(--band-dark);
    display: flex;
    align-items: center;
    justify-content: center;
  }
  .brand {
    display: flex;
    align-items: center;
    gap: 22px;
    margin-left: -20px;
  }
  .brand-mark {
    width: 62px;
    height: 62px;
    border-radius: 50%;
    border: 5px solid var(--brand-copper);
    box-sizing: border-box;
  }
  .brand-name {
    color: var(--brand-copper);
    font-weight: 600;
    line-height: 1;
    text-transform: uppercase;
  }
  .brand-name .line-main {
    display: block;
    font-size: 44px;
    letter-spacing: 1px;
  }
  .brand-name .line-tier {
    display: block;
    font-size: 22px;
    letter-spacing: 7px;
    margin-top: 6px;
  }
  .title-band {
    position: absolute;
    top: 320px;
    left: 0;
    width: 927px;
    height: 184px;
    background: var(--band-mid);
  }
  .title {
    position: absolute;
    top: 326px;
    left: 0;
    width: 927px;
    margin: 0;
    text-align: center;
    color: var(--ink-white);
    font-weight: 800;
    font-size: 106px;
    line-height: 1;
    letter-spacing: -1px;
  }
  .subtitle {
    position: absolute;
    top: 438px;
    left: 0;
    width: 927px;
    margin: 0;
    text-align: center;
    color: var(--ink-white);
    font-weight: 300;
    font-size: 46px;
    line-height: 1;
    letter-spacing: 1px;
  }
  .year {
    position: absolute;
    top: 520px;
    left: 0;
    width: 927px;
    margin: 0;
    text-align: center;
    color: var(--ink-white);
    font-weight: 800;
    font-size: 132px;
    line-height: 1;
    letter-spacing: 2px;
  }
</style>
</head>
<body>
  <main class="cover">
    <div class="cover-artwork" role="img" aria-label="Rusted steampunk machinery: brass clock face, interlocking gears, copper pipes and a shower of grinding sparks"></div>

    <header class="masthead">
      <div class="brand">
        <span class="brand-mark" aria-hidden="true"></span>
        <div class="brand-name">
          <span class="line-main">Torvak</span>
          <span class="line-tier">Brimvale</span>
        </div>
      </div>
    </header>

    <div class="title-band" aria-hidden="true"></div>
    <h1 class="title">CATALOGUE</h1>
    <p class="subtitle">FABRICATION PRODUCTS</p>
    <p class="year">2018</p>
  </main>
</body>
</html>
```